Postcard Mailing 1

Our website is qrtechaid.net
We travel on site to help people/businesses with their computer issues.
This postcard is going to existing customers... just trying to touch them again.
QRT Technic provides a full line of residential and commercial computer support.

I've attached some stuff that I have done.

```html
<!DOCTYPE html>
<html lang="en">
<head>
<meta charset="utf-8">
<title>QRT Technic – Postcard Mailing</title>
<link rel="stylesheet" href="https://fonts.googleapis.com/css2?family=EB+Garamond:ital,wght@1,400&family=Questrial&family=Archivo+Black&display=swap">
<style>
  :root {
    --page: #e6e6e4;
    --card: #ffffff;
    --purple: #a13d95;
    --purple-dark: #7e2b77;
    --purple-light: #c46cb8;
    --navy: #2b3a8c;
    --swoosh: #b8bfd8;
    --swoosh-deep: #8f97bd;
    --swoosh-pale: #dfe3f0;
    --gold: #b08a3c;
    --red: #d8231c;
    --green: #8cc63f;
    --green-dark: #5f9a22;
    --grey-box: #e9e9ea;
    --text-dark: #333333;
  }
  * { box-sizing: border-box; margin: 0; padding: 0; }
  html, body { width: 900px; height: 1200px; overflow: hidden; background: var(--page); }
  .canvas { position: relative; width: 900px; height: 1200px; }

  .card { position: absolute; background: var(--card); overflow: hidden; box-shadow: 0 3px 10px rgba(0,0,0,.25); }
  .card-front { left: 82px; top: 35px; width: 738px; height: 574px; }
  .card-back { left: 82px; top: 629px; width: 588px; height: 458px; }
  .swooshes { position: absolute; inset: 0; width: 100%; height: 100%; }

  .testimonial-photo { position: absolute; left: 0; top: 0; width: 111px; height: 114px;
    background: linear-gradient(160deg, #e8d3a6, #c9a884 55%, #f3efe8); }
  .testimonial-quote { position: absolute; left: 121px; top: 52px; white-space: nowrap;
    font-family: "EB Garamond", serif; font-style: italic; font-size: 19px; line-height: 27px; color: var(--gold); }

  .problem-photo { position: absolute; left: 14px; top: 171px; width: 300px; height: 300px; border-radius: 50%;
    background: linear-gradient(135deg, #6f7a86, #c9ccd0 45%, #f2f2f2 70%, #3a3d44); }
  .no-sign { position: absolute; left: 0; top: 157px; width: 328px; height: 328px; }

  .service-list { position: absolute; left: 0; top: 256px; width: 738px; list-style: none; }
  .service { position: relative; height: 33px; margin-bottom: 11px; }
  .service-band { position: absolute; top: 0; height: 33px;
    background: linear-gradient(90deg, rgba(161,61,149,.35), var(--purple) 30%, var(--purple-dark));
    clip-path: polygon(12px 0, 100% 0, calc(100% - 12px) 100%, 0 100%);
    color: #fff; font-family: "Questrial", sans-serif; font-size: 16px; letter-spacing: .6px; white-space: nowrap;
    display: flex; align-items: center; justify-content: flex-end; padding-right: 20px; }
  .service-icon { position: absolute; top: 2px; width: 29px; height: 29px; }

  .brand-front { position: absolute; left: 560px; top: 490px; display: flex; align-items: center; gap: 8px;
    font-family: "Questrial", sans-serif; font-size: 24px; color: var(--swoosh-deep); white-space: nowrap; }
  .brand-mark { width: 13px; height: 13px; background: var(--swoosh-deep); flex: none; }

  .brand-back { position: absolute; left: 22px; top: 40px; display: flex; align-items: center; gap: 7px;
    font-family: "Questrial", sans-serif; font-size: 20px; color: var(--navy); white-space: nowrap; }
  .brand-back .brand-mark { width: 12px; height: 12px; background: var(--navy); }
  .contact { position: absolute; left: 176px; top: 32px; font-family: "Questrial", sans-serif; color: var(--navy); font-weight: 700; white-space: nowrap; }
  .contact-web { font-size: 15px; line-height: 20px; }
  .contact-phone { font-size: 17px; line-height: 22px; margin-top: 2px; margin-left: 28px; }

  .offer { position: absolute; left: 14px; top: 97px; width: 271px; height: 281px;
    border: 3px solid #4a4f8c; border-radius: 8px; overflow: hidden;
    background: linear-gradient(180deg, #f7f7f7, var(--grey-box)); font-family: "Questrial", sans-serif; text-align: center; }
  .offer-header { background: linear-gradient(180deg, var(--purple-light), var(--purple)); color: #fff;
    font-size: 19px; line-height: 24px; padding: 5px 0 3px; letter-spacing: .5px; }
  .offer-header strong { font-family: "Archivo Black", sans-serif; font-size: 22px; font-weight: 400; }
  .offer-intro { font-size: 12px; color: var(--text-dark); margin-top: 10px; }
  .offer-items { list-style: none; font-size: 13.5px; color: var(--text-dark); line-height: 19px; margin-top: 4px; }
  .offer-icons { display: flex; justify-content: center; gap: 9px; margin-top: 8px; }
  .offer-icons svg { width: 28px; height: 28px; }
  .offer-price { margin: 10px auto 0; width: 240px; height: 32px; border-radius: 6px;
    background: linear-gradient(180deg, #a9d86a, var(--green-dark)); color: #fff; font-size: 17px; line-height: 32px; }
  .offer-support { font-size: 12px; color: var(--text-dark); margin-top: 6px; }
  .offer-housecalls { font-size: 12px; color: #5a6a9a; margin-top: 2px; }

  .address-lines { position: absolute; left: 291px; top: 212px; width: 279px; }
  .address-lines span { display: block; height: 1px; background: #444; margin-bottom: 34px; }

  .guarantee { position: absolute; left: 35px; top: 402px; font-family: "EB Garamond", serif; font-style: italic;
    font-size: 16px; color: var(--navy); white-space: nowrap; }
</style>
</head>
<body>
<main class="canvas">

  <section class="card card-front">
    <svg class="swooshes" viewBox="0 0 738 574" aria-hidden="true">
      <path d="M0 120 C 180 105, 330 120, 480 60 C 580 20, 660 5, 738 0 L738 60 C 620 70, 480 120, 0 140 Z" fill="#d6eef0" opacity=".7"/>
      <path d="M120 574 C 260 360, 480 180, 738 110 L738 200 C 520 250, 330 400, 230 574 Z" fill="var(--swoosh)" opacity=".55"/>
      <path d="M40 574 C 220 380, 430 170, 738 60 L738 110 C 470 190, 260 380, 140 574 Z" fill="var(--swoosh-deep)" opacity=".55"/>
      <path d="M330 574 C 420 420, 560 330, 738 300 L738 360 C 590 390, 470 470, 420 574 Z" fill="var(--swoosh-pale)"/>
      <path d="M300 80 C 430 140, 560 200, 738 190" stroke="var(--swoosh)" stroke-width="18" fill="none" opacity=".6"/>
      <path d="M640 574 C 680 450, 700 380, 738 330 L738 574 Z" fill="var(--swoosh-pale)"/>
      <path d="M560 574 C 620 420, 680 250, 700 0" stroke="#cfe0ef" stroke-width="10" fill="none"/>
    </svg>

    <div class="testimonial-photo" role="img" aria-label="Portrait of a smiling satisfied customer"></div>
    <p class="testimonial-quote">"QRT's $19.95 a month computer protection<br>and support plan gives us peace of mind."</p>

    <div class="problem-photo" role="img" aria-label="Photo of a frustrated woman with her head in her hands at a computer desk"></div>
    <svg class="no-sign" viewBox="0 0 328 328" aria-hidden="true">
      <circle cx="164" cy="164" r="146" fill="none" stroke="var(--red)" stroke-width="30"/>
      <line x1="61" y1="267" x2="267" y2="61" stroke="var(--red)" stroke-width="30"/>
    </svg>

    <ul class="service-list">
      <li class="service"><span class="service-band" style="left:318px;width:328px">VIRUS / SPYWARE CLEANUP</span>
        <svg class="service-icon" style="left:654px" viewBox="0 0 30 30"><path d="M15 3 L26 7 V15 C26 22 21 26 15 28 C9 26 4 22 4 15 V7 Z" fill="var(--purple)"/><path d="M15 6 V25 C10 23 7 20 7 15 V9 Z" fill="#fff" opacity=".6"/></svg></li>
      <li class="service"><span class="service-band" style="left:318px;width:316px">COMPUTER SETUP</span>
        <svg class="service-icon" style="left:640px" viewBox="0 0 30 30"><circle cx="15" cy="15" r="9" fill="none" stroke="var(--purple)" stroke-width="5" stroke-dasharray="4 3"/><circle cx="15" cy="15" r="6" fill="var(--purple)"/><circle cx="15" cy="15" r="2.5" fill="#fff"/></svg></li>
      <li class="service"><span class="service-band" style="left:318px;width:301px">WIRELESS NETWORKS</span>
        <svg class="service-icon" style="left:628px" viewBox="0 0 30 30"><path d="M3 12 Q15 2 27 12" stroke="var(--purple)" stroke-width="3" fill="none"/><path d="M8 17 Q15 10 22 17" stroke="var(--purple)" stroke-width="3" fill="none"/><circle cx="15" cy="23" r="3" fill="var(--purple)"/></svg></li>
      <li class="service"><span class="service-band" style="left:306px;width:301px">DATA TRANSFER / RECOVERY</span>
        <svg class="service-icon" style="left:618px" viewBox="0 0 30 30"><rect x="4" y="3" width="12" height="16" fill="none" stroke="var(--purple)" stroke-width="2"/><rect x="14" y="11" width="12" height="16" fill="#fff" stroke="var(--purple)" stroke-width="2"/><path d="M8 22 L8 26 L12 26" stroke="var(--purple)" stroke-width="2" fill="none"/></svg></li>
    </ul>

    <div class="brand-front"><span class="brand-mark"></span>QRT Technic</div>
  </section>

  <section class="card card-back">
    <svg class="swooshes" viewBox="0 0 588 458" aria-hidden="true">
      <path d="M200 0 C 320 120, 460 250, 588 300 L588 360 C 440 300, 300 170, 170 0 Z" fill="var(--swoosh-pale)" opacity=".8"/>
      <path d="M280 458 C 360 360, 470 300, 588 280 L588 320 C 480 340, 390 390, 330 458 Z" fill="var(--swoosh-pale)"/>
      <path d="M0 60 C 200 80, 400 180, 588 200" stroke="#eceef6" stroke-width="22" fill="none"/>
      <path d="M100 458 C 260 380, 430 350, 588 380" stroke="#eef0f7" stroke-width="16" fill="none"/>
    </svg>

    <div class="brand-back"><span class="brand-mark"></span>QRT Technic</div>
    <div class="contact">
      <p class="contact-web">www.qrtechaid.net</p>
      <p class="contact-phone">(555) 013-4820</p>
    </div>

    <div class="offer">
      <p class="offer-header">CALL US TODAY<br>FOR A <strong>20%</strong> DISCOUNT!</p>
      <p class="offer-intro">QRT takes care of</p>
      <ul class="offer-items">
        <li>VIRUS PROTECTION</li>
        <li>DATA BACKUPS</li>
        <li>NIMBUS OS UPDATES</li>
      </ul>
      <div class="offer-icons">
        <svg viewBox="0 0 28 28"><path d="M14 2 L25 6 V14 C25 21 20 25 14 27 C8 25 3 21 3 14 V6 Z" fill="#111"/><path d="M14 2 V14 H3 V6 Z M14 14 H25 C25 21 20 25 14 27 Z" fill="#f2c500"/></svg>
        <svg viewBox="0 0 28 28"><circle cx="14" cy="14" r="9" fill="none" stroke="#888" stroke-width="5" stroke-dasharray="4 3"/><circle cx="14" cy="14" r="6" fill="#999"/><circle cx="14" cy="14" r="2.5" fill="#eee"/></svg>
        <svg viewBox="0 0 28 28"><path d="M2 11 Q14 1 26 11" stroke="var(--green)" stroke-width="3" fill="none"/><path d="M7 16 Q14 9 21 16" stroke="var(--green)" stroke-width="3" fill="none"/><circle cx="14" cy="22" r="3" fill="var(--green)"/></svg>
        <svg viewBox="0 0 28 28"><rect x="3" y="2" width="12" height="16" fill="#fff" stroke="#222" stroke-width="2"/><rect x="13" y="10" width="12" height="16" fill="#fff" stroke="#222" stroke-width="2"/><path d="M6 21 L6 25 L10 25" stroke="var(--red)" stroke-width="2" fill="none"/></svg>
        <svg viewBox="0 0 28 28"><rect x="3" y="3" width="22" height="22" fill="#f25022"/></svg>
      </div>
      <p class="offer-price">JUST $19.95 A MONTH!</p>
      <p class="offer-support">* Unlimited Support *</p>
      <p class="offer-housecalls">We Also Make Housecalls!</p>
    </div>

    <div class="address-lines"><span></span><span></span><span></span><span></span></div>

    <p class="guarantee">"If We Can't Fix It...You Don't Pay!"</p>
  </section>

</main>
</body>
</html>
```